Outdoor Company Business Card design

We are an outdoor adventure company needing a business card. We sell outdoor adventures and clothing. Please use our logo in the business card. We are looking for something unique but delivers a clear message as to who we are. Please be creative

Target Market(s)

Outdoor adventures

Industry/Entity Type

Business

Contact Information for Business Card

Business name: TrailBrook If using the logo, no need to have a spot for the name
Owner / CEO: Owen Pardle
Website: TrailBrook.example
Social.example: Social.example/TrailBrook
Instagram: @pardle_owen
phone number: 555-384-7120
Email: Pardleteams@TrailBrook.example

Colors

Designer to choose colors to be used in the design.

Requirements
Must have
• The business card must include the details mentioned above. ie logo, my name, email, facebook, instagram, website, and phone number.
Should not have
• should not be cluttered or look messy

```html
<!DOCTYPE html>
<html lang="en">
<head>
<meta charset="utf-8">
<title>TrailBrook Business Card</title>
<link rel="stylesheet" href="https://fonts.googleapis.com/css2?family=Lato:wght@400;700;900&display=swap">
<style>
  :root {
    --brand-blue: #1e74bc;
    --brand-orange: #f05a28;
    --paper: #ffffff;
    --backdrop: #e9e7e4;
    --ink-light: #ffffff;
  }
  * { margin: 0; padding: 0; box-sizing: border-box; }
  html, body {
    width: 1200px; height: 900px; overflow: hidden;
    background: var(--backdrop);
    font-family: "Lato", Arial, sans-serif;
  }
  .canvas { position: relative; width: 1200px; height: 900px; }
  .card {
    position: absolute;
    box-shadow: 0 6px 18px rgba(0,0,0,0.18);
    overflow: hidden;
  }
  .card-front { left: 178px; top: 73px; width: 588px; height: 365px; background: var(--paper); }
  .card-back { left: 388px; top: 505px; width: 567px; height: 352px; background: var(--brand-blue); }
  .front-shapes { position: absolute; inset: 0; }

  .wordmark {
    position: absolute; left: 0; right: 0;
    display: flex; align-items: center; justify-content: center; gap: 14px;
    font-weight: 900; text-transform: uppercase; letter-spacing: 1px;
    line-height: 1;
  }
  .wordmark-dot { width: 22px; height: 22px; border-radius: 50%; flex: none; }
  .card-front .wordmark { top: 122px; font-size: 42px; color: var(--brand-blue); }
  .card-front .wordmark-dot { background: var(--brand-orange); }
  .card-back .wordmark { top: 200px; font-size: 44px; color: var(--ink-light); }
  .card-back .wordmark-dot { background: var(--ink-light); }

  .owner { position: absolute; right: 35px; top: 221px; text-align: right; color: var(--ink-light); }
  .owner-name { font-size: 19px; font-weight: 700; letter-spacing: 1px; text-transform: uppercase; line-height: 1.1; }
  .owner-title { font-size: 15px; font-weight: 400; }

  .contact-list {
    position: absolute; right: 36px; top: 279px;
    list-style: none; color: var(--ink-light); font-size: 16px; text-align: right;
  }
  .contact-list li { display: flex; align-items: center; justify-content: flex-end; gap: 6px; height: 21px; }
  .contact-icon { width: 12px; height: 12px; flex: none; }

  .social-list {
    position: absolute; left: 18px; top: 298px;
    list-style: none; color: var(--ink-light); font-size: 16px;
  }
  .social-list li { display: flex; align-items: center; gap: 7px; height: 23px; }
  .social-mark { width: 16px; height: 16px; background: var(--ink-light); border-radius: 2px; flex: none; }
</style>
</head>
<body>
<main class="canvas">
  <section class="card card-front" aria-label="Business card front">
    <svg class="front-shapes" width="588" height="365" viewBox="0 0 588 365" aria-hidden="true">
      <polygon points="0,199 404,199 384,226 0,226" fill="var(--brand-orange)"/>
      <polygon points="418,192 588,192 588,365 0,365 0,230 388,230" fill="var(--brand-blue)"/>
    </svg>
    <div class="wordmark"><span class="wordmark-dot"></span><span>TrailBrook</span></div>
    <div class="owner">
      <p class="owner-name">Owen Pardle</p>
      <p class="owner-title">Owner / CEO</p>
    </div>
    <ul class="contact-list">
      <li>555-384-7120
        <svg class="contact-icon" viewBox="0 0 12 12" aria-hidden="true"><path d="M1 4 Q6 0 11 4 L9.5 5.5 L8 4.5 L8 3.5 Q6 3 4 3.5 L4 4.5 L2.5 5.5 Z M3 6 H9 L10 11 H2 Z" fill="#fff"/></svg>
      </li>
      <li>Pardleteams@TrailBrook.example
        <svg class="contact-icon" viewBox="0 0 12 12" aria-hidden="true"><rect x="0.5" y="2" width="11" height="8" fill="#fff"/><path d="M0.5 2 L6 6.5 L11.5 2" fill="none" stroke="var(--brand-blue)" stroke-width="1"/></svg>
      </li>
      <li>www.TrailBrook.example
        <svg class="contact-icon" viewBox="0 0 12 12" aria-hidden="true"><circle cx="6" cy="6" r="5.5" fill="#fff"/><ellipse cx="6" cy="6" rx="2.2" ry="5.5" fill="none" stroke="var(--brand-blue)" stroke-width="0.8"/><line x1="0.5" y1="6" x2="11.5" y2="6" stroke="var(--brand-blue)" stroke-width="0.8"/></svg>
      </li>
    </ul>
    <ul class="social-list">
      <li><span class="social-mark"></span>Social.example/TrailBrook</li>
      <li><span class="social-mark"></span>@pardle_owen</li>
    </ul>
  </section>

  <section class="card card-back" aria-label="Business card back">
    <div class="wordmark"><span class="wordmark-dot"></span><span>TrailBrook</span></div>
  </section>
</main>
</body>
</html>
```